Alpenmark Banner

Hi boys and girls :)

We have a little project 4u.

We need a banner in 4 sizes :

Leaderboard: 728*90
Wide SkyScraper: 160*600
Medium Rectangle: 300*250
Ribbon (special format): 990*45

Message on banner :

Either our Logo + Immigration, Integration, Naturalization

Or our Logo + Incorporation, Domicile, Secretarial Services

And if space allows for it www.alpenmark-example.com as well.

We are looking for a clean design, check our Website for inspiration concerning colors.

```html
<!DOCTYPE html>
<html lang="en">
<head>
<meta charset="utf-8">
<title>Alpenmark Leaderboard Banner</title>
<link href="https://fonts.googleapis.com/css2?family=Archivo+Narrow:wght@500&family=Libre+Baskerville&family=Arimo&display=swap" rel="stylesheet">
<style>
  :root {
    --panel-white: #ffffff;
    --band-top: #3d3d3d;
    --band-top-dark: #2f2f2f;
    --band-bottom: #2a2a2a;
    --accent-red: #e3171f;
    --text-light: #ffffff;
    --link-blue: #4a5ff0;
    --logo-ink: #1f1f1f;
  }
  html, body {
    margin: 0;
    padding: 0;
    width: 1200px;
    height: 148px;
    overflow: hidden;
    background: var(--panel-white);
  }
  .banner {
    position: relative;
    width: 1200px;
    height: 148px;
    overflow: hidden;
  }
  .brand-panel {
    position: absolute;
    left: 0; top: 0;
    width: 297px;
    height: 148px;
    background: var(--panel-white);
    display: flex;
    align-items: center;
    justify-content: center;
  }
  .brand-name {
    font-family: "Libre Baskerville", serif;
    font-size: 34px;
    color: var(--logo-ink);
    letter-spacing: 1px;
  }
  .accent-rule {
    position: absolute;
    left: 297px; top: 0;
    width: 903px;
    height: 5px;
    background: var(--accent-red);
  }
  .services-band {
    position: absolute;
    left: 297px; top: 5px;
    width: 903px;
    height: 97px;
    background: linear-gradient(to bottom, var(--band-top), var(--band-top-dark));
    border-bottom: 1px solid #555;
  }
  .service {
    position: absolute;
    top: 26px;
    transform: translateX(-50%);
    font-family: "Archivo Narrow", sans-serif;
    font-weight: 500;
    font-variant: small-caps;
    font-size: 38px;
    line-height: 1;
    color: var(--text-light);
    letter-spacing: 0.5px;
    white-space: nowrap;
  }
  .service--immigration { left: 189px; }
  .service--integration { left: 448px; color: var(--accent-red); }
  .service--naturalization { left: 708px; }
  .web-band {
    position: absolute;
    left: 297px; top: 103px;
    width: 903px;
    height: 45px;
    background: var(--band-bottom);
  }
  .web-address {
    position: absolute;
    left: 453px; top: 7px;
    transform: translateX(-50%);
    font-family: "Arimo", sans-serif;
    font-size: 27px;
    color: var(--link-blue);
    white-space: nowrap;
  }
</style>
</head>
<body>
  <div class="banner">
    <div class="brand-panel">
      <span class="brand-name">ALPENMARK</span>
    </div>
    <div class="accent-rule"></div>
    <div class="services-band">
      <span class="service service--immigration">Immigration</span>
      <span class="service service--integration">Integration</span>
      <span class="service service--naturalization">Naturalization</span>
    </div>
    <div class="web-band">
      <span class="web-address">www.alpenmark-example.com</span>
    </div>
  </div>
</body>
</html>
```